Vintage themed home decor Shopify store needs sales promotion banner ads

"Quill & Lantern Goods" is an Australian based lifestyle home decor store that sells vintage, retro and antique relic replicas and reproduction items online to their local customers Australia wide.

We need banner ads for our store home page slider that promotes our unique products, new stock arrival and calls store visitors to to buy from our different product collections.

We anticipate that we will need multiple banner ads, primarily for the following product collections:
1. Sundials & Compass
2. Airplane models
3. Magnifying glass
4. Clocks & Watches

Banners could also be generic with generic discount coupon promotions.

Banners should be based around the theme of our store and products which gives a sense of colonial / vintage lifestyle and that they compliment the colour & theme of the store.

Banner Size: 1600 x 800 px

Please find attached some samples of the types of banner ads we have in mind and also our logo. Product images can be supplied if they are required to be used in the ads.

Website URL: https://quillandlanterngoods.example

Target Market(s)

mostly Males aged between 35-65.
Products ideally for man-cave & office decor.

Industry/Entity Type

Home And Garden

Font styles to use
Serif
Decorative
Script

Requirements
Must have
• some product images
Nice to have
• lifestyle shots.
• blank space to insert for a coupon code
Should not have
• caricatures & cartoon

```html
<!DOCTYPE html>
<html lang="en">
<head>
<meta charset="UTF-8">
<title>Sundials &amp; Compass Promotion Banner</title>
<link href="https://fonts.googleapis.com/css2?family=Arimo:wght@400;700&display=swap" rel="stylesheet">
<style>
  :root {
    --promo-red: #e00000;
    --oval-red: #d9363e;
    --oval-fill: rgba(235, 228, 222, 0.72);
    --ink: #2f2f2f;
    --white: #ffffff;
    --button-blue: #0a52e6;
    --hex-frame: #5c5c5e;
    --room-light: #e8e1d8;
    --room-mid: #b9a58f;
    --room-dark: #5a3a28;
    --table-grey: #8d8a85;
  }
  html, body {
    margin: 0;
    padding: 0;
    width: 1200px;
    height: 600px;
    overflow: hidden;
    background: var(--white);
  }
  .banner {
    position: relative;
    width: 1200px;
    height: 600px;
    overflow: hidden;
    font-family: "Arimo", Arial, sans-serif;
  }
  .lifestyle-scene {
    position: absolute;
    inset: 0;
    background:
      linear-gradient(180deg, transparent 0%, transparent 84%, var(--table-grey) 86%, #6f6c68 100%),
      linear-gradient(180deg, var(--room-light) 0%, var(--room-light) 32%, var(--room-mid) 45%, var(--room-dark) 62%, #6a4632 84%),
      linear-gradient(90deg, #d8cfc4 0%, #efe9e2 60%, #f4f2ef 100%);
    background-blend-mode: normal, multiply, normal;
  }
  .collection-oval {
    position: absolute;
    left: 0;
    top: 0;
  }
  .collection-copy {
    position: absolute;
    left: 62px;
    width: 304px;
    text-align: center;
    color: var(--ink);
  }
  .collection-title {
    top: 160px;
    margin: 0;
    font-size: 29px;
    font-weight: 700;
    line-height: 31px;
  }
  .collection-tagline {
    top: 269px;
    margin: 0;
    font-size: 23px;
    font-weight: 400;
    line-height: 33px;
  }
  .shop-button {
    position: absolute;
    left: 144px;
    top: 398px;
    width: 141px;
    height: 41px;
    border-radius: 3px;
    background: var(--button-blue);
    color: var(--white);
    font-size: 20px;
    line-height: 41px;
    text-align: center;
    text-decoration: none;
  }
  .promo-box {
    position: absolute;
    left: 354px;
    top: 183px;
    width: 229px;
    height: 232px;
    background: var(--promo-red);
    color: var(--white);
    font-weight: 700;
  }
  .promo-lead {
    position: absolute;
    left: 0;
    width: 100%;
    top: 17px;
    text-align: center;
    font-size: 17px;
    letter-spacing: 0.3px;
  }
  .promo-percent {
    position: absolute;
    left: 16px;
    top: 30px;
    font-size: 124px;
    line-height: 124px;
    letter-spacing: -3px;
  }
  .promo-sign {
    position: absolute;
    left: 156px;
    top: 41px;
    font-size: 72px;
    line-height: 72px;
  }
  .promo-off {
    position: absolute;
    left: 158px;
    top: 110px;
    font-size: 27px;
    line-height: 30px;
    font-weight: 400;
  }
  .promo-code-label {
    position: absolute;
    left: 0;
    width: 100%;
    top: 152px;
    text-align: center;
    font-size: 17px;
  }
  .promo-code {
    position: absolute;
    left: 0;
    width: 100%;
    top: 177px;
    text-align: center;
    font-size: 35px;
    line-height: 40px;
    letter-spacing: 0.5px;
  }
  .product-tiles {
    position: absolute;
    left: 0;
    top: 0;
  }
</style>
</head>
<body>
  <main class="banner">
    <div class="lifestyle-scene" role="img" aria-label="Lifestyle photo of a vintage living room with a leather chesterfield sofa, brass armillary sphere and decor on a grey wooden coffee table"></div>

    <svg class="collection-oval" width="1200" height="600" viewBox="0 0 1200 600" aria-hidden="true">
      <ellipse cx="207" cy="300" rx="151" ry="214" fill="var(--oval-fill)" stroke="var(--oval-red)" stroke-width="7"/>
    </svg>

    <h1 class="collection-copy collection-title">Sundials &amp;<br>Compass</h1>
    <p class="collection-copy collection-tagline">Our Collection will<br>give you satisfaction</p>
    <a class="shop-button" href="https://quillandlanterngoods.example">Shop Now</a>

    <section class="promo-box">
      <div class="promo-lead">TAKE THIS CHANCE:</div>
      <div class="promo-percent">50</div>
      <div class="promo-sign">%</div>
      <div class="promo-off">OFF</div>
      <div class="promo-code-label">USE COUPON CODE :</div>
      <div class="promo-code">QUILL018</div>
    </section>

    <svg class="product-tiles" width="1200" height="600" viewBox="0 0 1200 600">
      <defs>
        <radialGradient id="brass-tone" cx="50%" cy="50%" r="50%">
          <stop offset="0%" stop-color="#b89a62"/>
          <stop offset="70%" stop-color="#8a6f3e"/>
          <stop offset="100%" stop-color="#f4f1ec"/>
        </radialGradient>
        <radialGradient id="bronze-tone" cx="50%" cy="50%" r="50%">
          <stop offset="0%" stop-color="#7a6446"/>
          <stop offset="70%" stop-color="#5a4632"/>
          <stop offset="100%" stop-color="#f4f1ec"/>
        </radialGradient>
      </defs>
      <g class="product-tile">
        <polygon points="893,18 1014,94 1014,252 893,328 772,252 772,94" fill="var(--white)" stroke="var(--hex-frame)" stroke-width="8"/>
        <polygon points="893,30 1004,100 1004,246 893,316 782,246 782,100" fill="url(#brass-tone)" role="img" aria-label="Product photo of a brass pocket sundial compass"/>
      </g>
      <g class="product-tile">
        <polygon points="1022,272 1144,348 1144,506 1022,582 900,506 900,348" fill="var(--white)" stroke="var(--hex-frame)" stroke-width="8"/>
        <polygon points="1022,284 1134,354 1134,500 1022,570 910,500 910,354" fill="url(#bronze-tone)" role="img" aria-label="Product photo of a bronze nautical sundial compass with raised gnomon"/>
      </g>
    </svg>
  </main>
</body>
</html>
```